Roofing & Siding door hanger flyer

-Looking to make door hanger flyer for Pellmont Roofing & Siding
-4.5" wide x 11" tall
-2 sided full colour
-We have started a new website (the content is changing) I have attached photos.
-About us:
-25 year labour warranty's available
-32 years in Calgary
-QCR A+ Member
-NWTG (Prairie Joint Shingle Guild) (logo attached)
-KOV Summit Select (logo attached)
-Owen Brisket (logo attached)
-Slogan "Raised On Care, Proven Through Seasons" 32 years in Calgary
-Sale
-Page 1 & 2 design ideas
We are in your area, contact us today for your Exclusive limited time offer! *discounts apply exclusively to new agreements only
Updates
-Please keep simple, clean & bright
-I really like the bright blue from our new logo (new logo uploaded)
-We specialize in Roofing -Siding-Gutters & full Exterior Renos (like the competitor example uploaded)
-This is the NEW website we are currently working on (not finished) https://mockview.example-draftpad.net/view/1a2b3c4d-5e6f-4a7b-8c9d-0e1f2a3b4c5d-7k2m/?fullscreen
-This is our OLD website https://pellmontshingleworks.com
-For the sale "We are in your area, contact us today for your Exclusive limited time offer" *discounts apply exclusively to new agreements only
-Free Estimates
-our phone# is 403-555-0148
-our website is pellmontshingleworks.com
-keep simple, clean, bright use the "new logo" uploaded. Check out the competitor example uploaded file
-We are in your area, Contact us today for your Exclusive limited time offer! *discounts apply to new agreements only
-FREE ESTIMATES
-Specialized in Roofing /Siding /Gutters Full Exterior Reno's
-We are currently working on a NEW website https://mockview.example-draftpad.net/view/1a2b3c4d-5e6f-4a7b-8c9d-0e1f2a3b4c5d-7k2m/?fullscreen
-Our OLD website https://pellmontshingleworks.com/
-Post old site address on flyer pellmontshingleworks.com
-Phone # 403-555-0148
Target Market(s)
40-55
Industry/Entity Type
Roofing Siding & full Exterior Reno's
Look and feel

```html
<!DOCTYPE html>
<html lang="en">
<head>
<meta charset="utf-8">
<title>Pellmont Roofing &amp; Siding – Door Hanger</title>
<link rel="stylesheet" href="https://fonts.googleapis.com/css2?family=Poppins:wght@300;400;500;600;700;800&family=Oswald:wght@500;600&display=swap">
<style>
:root{
  --page:#3d3d3d;
  --blue:#148cf0;
  --blue-deep:#0f6bd0;
  --navy:#1c4f8c;
  --ink-blue:#0a55b8;
  --sky:#a9dcfa;
  --red:#e2262b;
  --red-dark:#9e1a1e;
  --ink:#3a3a3a;
  --white:#ffffff;
  --gold:#d6a526;
}
*{margin:0;padding:0;box-sizing:border-box}
html,body{width:1200px;height:1117px;overflow:hidden;background:var(--page)}
body{position:relative;font-family:"Poppins",sans-serif}
.hanger{position:absolute;top:75px;width:399px;height:971px;background:var(--white);overflow:hidden;box-shadow:6px 8px 18px rgba(0,0,0,.45)}
.hanger--front{left:224px}
.hanger--back{left:656px}
.abs{position:absolute}
.die-cut{position:absolute;left:0;top:0}
.headline{position:absolute;top:20px;left:0;width:100%;text-align:center;color:var(--white);font-weight:800;font-size:17.5px;letter-spacing:-.2px}
.photo{position:absolute}
.photo--front-house{left:0;top:0;width:399px;height:330px;background:linear-gradient(160deg,#cfe3f5 0%,#8d97a8 40%,#6d6a66 70%,#6f9a44 100%);clip-path:polygon(255px 92px,306px 54px,399px 100px,399px 328px,330px 232px,268px 165px)}
.brand{position:absolute;left:0;width:100%;text-align:center}
.brand__est{top:249px;font-size:14px;letter-spacing:2px;color:#222;font-weight:400}
.brand__name{top:266px;font-size:44px;font-weight:800;color:#111;letter-spacing:1px;line-height:1}
.brand__mark{display:inline-block;width:22px;height:22px;background:var(--blue);margin-right:10px;vertical-align:6px}
.brand__trade{top:321px;font-size:22px;font-weight:300;letter-spacing:5.5px;color:#333}
.service{position:absolute;left:25px;width:374px}
.service__label{position:absolute;left:0;top:0;width:57px;height:100%;background:var(--navy)}
.service__label span{position:absolute;left:50%;top:50%;transform:translate(-50%,-50%) rotate(-90deg);white-space:nowrap;color:var(--white);font-family:"Oswald",sans-serif;font-weight:500;font-size:25px;letter-spacing:.5px}
.service__photo{position:absolute;left:57px;top:0;width:119px;height:100%}
.service__list{position:absolute;left:176px;top:0;right:0;height:100%;background:linear-gradient(to bottom,var(--sky),var(--white) 50%)}
.roofing{top:360px;height:164px}
.roofing .service__photo{background:linear-gradient(to bottom,#c9d7e4 0%,#dfe6ec 35%,#5c6470 65%,#3e444c 100%)}
.siding{top:529px;height:163px}
.siding .service__photo{background:linear-gradient(135deg,#5d9ee6 0%,#cfdbe6 35%,#f2f4f6 70%,#dde3e8 100%)}
.exterior{top:697px;height:171px}
.exterior .service__list{left:57px;background:linear-gradient(to bottom,var(--sky),var(--white) 40%)}
.item{position:absolute;font-size:13.5px;font-weight:600;color:var(--ink);line-height:15px;padding-left:19px}
.item::before{content:"";position:absolute;left:0;top:3px;width:9px;height:9px;border:1px solid var(--navy);border-radius:50%}
.item::after{content:"";position:absolute;left:3px;top:5px;width:3px;height:4px;border:solid var(--navy);border-width:0 1px 1px 0;transform:rotate(40deg)}
.item small{display:block;font-size:13px;font-weight:400;line-height:15.5px}
.footer-band{position:absolute;left:0;top:868px;width:100%;height:103px;background:var(--blue)}
.estimates{position:absolute;left:82px;top:845px;width:234px;height:39px;background:var(--red);box-shadow:5px 5px 0 var(--red-dark);text-align:center;color:var(--white);font-family:"Oswald",sans-serif;font-weight:600;font-size:29px;line-height:39px;letter-spacing:.3px}
.phone{position:absolute;left:0;top:892px;width:100%;text-align:center;color:var(--white);font-weight:800;font-size:35px;line-height:44px;letter-spacing:-.5px}
.phone svg{vertical-align:-4px;margin-right:6px}
.website{position:absolute;left:0;top:931px;width:100%;text-align:center;color:var(--white);font-weight:600;font-size:15.5px;letter-spacing:.3px}
/* back */
.hanger--back{background:var(--white)}
.back-field{position:absolute;left:0;top:0}
.seal{position:absolute;left:270px;top:69px;width:100px;height:100px;border-radius:50%;background:radial-gradient(circle,#f3d36a 0%,var(--gold) 55%,#8a6410 100%);box-shadow:0 0 0 4px #e9c24a}
.warranty{position:absolute;left:32px;top:178px;width:162px;height:217px;border-radius:8px 8px 0 0;background:linear-gradient(to bottom,var(--blue-deep) 70%,rgba(15,107,208,0));color:var(--white);text-align:center}
.warranty__num{position:absolute;top:8px;left:0;width:100%;font-size:84px;font-weight:800;line-height:84px;letter-spacing:-3px}
.warranty__unit{position:absolute;top:96px;left:0;width:100%;font-size:36px;font-weight:700;line-height:36px}
.warranty__text{position:absolute;top:132px;left:0;width:100%;font-size:16.5px;font-weight:600;line-height:18px}
.motto{position:absolute;left:200px;top:212px;width:175px;text-align:center;color:var(--white);font-weight:800;font-size:21px;line-height:25px}
.motto__mark{display:block;font-size:20px;line-height:16px}
.photo--back-house{left:0;top:0;width:399px;height:640px;background:linear-gradient(to bottom,#9fcdf3 0%,#2c5fa8 40%,#1f4c8e 70%,#8b8a84 88%,#5f9a3d 100%);clip-path:polygon(0 420px,100px 370px,200px 418px,310px 383px,399px 418px,399px 585px,200px 636px,0 571px)}
.partners{position:absolute;left:14px;top:664px;width:372px;display:flex;justify-content:space-between;align-items:center}
.partner{display:flex;align-items:center;gap:5px;font-size:13px;font-weight:700;color:var(--navy);white-space:nowrap}
.partner i{display:block;width:10px;height:10px;background:var(--blue)}
.offer{position:absolute;left:0;width:100%;text-align:center}
.offer__lead{top:716px;font-size:21px;font-weight:800;color:var(--ink-blue)}
.offer__main{top:738px;font-size:37px;font-weight:800;color:var(--ink-blue);letter-spacing:-.5px}
.offer__sub{top:783px;font-size:16.5px;font-weight:800;color:#1580e8}
.offer__note{top:810px;font-size:10.5px;font-weight:500;color:#333}
</style>
</head>
<body>

<!-- FRONT -->
<section class="hanger hanger--front">
  <svg class="die-cut" width="399" height="180" viewBox="0 0 399 180" aria-hidden="true">
    <path d="M0 0H399V104C330 98 290 104 255 112H150C110 112 70 95 0 95Z" fill="var(--blue)"/>
    <path d="M0 95C70 95 110 112 150 112L150 124C105 118 60 122 0 136Z" fill="var(--page)"/>
    <circle cx="200" cy="115" r="55" fill="var(--page)"/>
  </svg>
  <div class="photo photo--front-house" role="img" aria-label="Photo of a grey two-storey house with a shingled roof and front porch"></div>
  <p class="headline">WE’RE IN YOUR NEIGHBOURHOOD!</p>

  <p class="brand brand__est">Est. 1991</p>
  <p class="brand brand__name"><span class="brand__mark"></span>PELLMONT</p>
  <p class="brand brand__trade">ROOFING &amp; SIDING</p>

  <div class="service roofing">
    <div class="service__label"><span>ROOFING</span></div>
    <div class="service__photo" role="img" aria-label="Photo of a dormer window on an asphalt shingle roof"></div>
    <div class="service__list">
      <p class="item" style="left:11px;top:48px">Asphalt</p>
      <p class="item" style="left:11px;top:77px">Rubber</p>
      <p class="item" style="left:11px;top:107px">Metal</p>
    </div>
  </div>

  <div class="service siding">
    <div class="service__label"><span>SIDING</span></div>
    <div class="service__photo" role="img" aria-label="Photo of white siding with soffit and downspout"></div>
    <div class="service__list">
      <p class="item" style="left:11px;top:34px">Brisket fibre cement</p>
      <p class="item" style="left:11px;top:58px">Vinyl</p>
      <p class="item" style="left:11px;top:82px">Metal<small>(Steel, Aluminum)<br>Longboard</small></p>
    </div>
  </div>

  <div class="service exterior">
    <div class="service__label"><span>FULL EXTERIOR</span></div>
    <div class="service__list">
      <p class="item" style="left:22px;top:31px">Eavesthrough/<br>Soffit/Fascia</p>
      <p class="item" style="left:22px;top:69px">Stone</p>
      <p class="item" style="left:22px;top:94px">Skylights</p>
      <p class="item" style="left:22px;top:119px">Windows &amp; Doors</p>
      <p class="item" style="left:175px;top:31px">Stucco</p>
      <p class="item" style="left:175px;top:56px">Insulation</p>
      <p class="item" style="left:175px;top:81px">Painting</p>
      <p class="item" style="left:175px;top:106px">Shake Repairs</p>
    </div>
  </div>

  <div class="footer-band"></div>
  <p class="estimates">FREE ESTIMATES</p>
  <p class="phone"><svg width="30" height="30" viewBox="0 0 30 30" aria-hidden="true"><circle cx="15" cy="15" r="15" fill="#fff"/><path d="M10.5 7.5l3 3.5-1.8 2.2c1 2 2.6 3.6 4.6 4.6l2.2-1.8 3.5 3-1.8 2.8c-6.5-.5-11.8-5.8-12.3-12.3z" fill="var(--blue)"/></svg>403-555-0148</p>
  <p class="website">www.pellmontshingleworks.com</p>
</section>

<!-- BACK -->
<section class="hanger hanger--back">
  <svg class="back-field" width="399" height="650" viewBox="0 0 399 650" aria-hidden="true">
    <path d="M0 0H399V595L200 645L0 580Z" fill="var(--blue)"/>
    <path d="M0 95C70 95 110 112 150 112L150 124C105 118 60 122 0 136Z" fill="var(--page)"/>
    <circle cx="200" cy="115" r="55" fill="var(--page)"/>
  </svg>
  <p class="headline" style="top:24px">WE’RE IN YOUR NEIGHBOURHOOD!</p>
  <div class="seal" role="img" aria-label="Gold 32-year anniversary seal"></div>

  <div class="warranty">
    <p class="warranty__num">25</p>
    <p class="warranty__unit">YEAR</p>
    <p class="warranty__text">LABOUR<br>WARRANTY'S<br>AVAILABLE</p>
  </div>

  <p class="motto"><span class="motto__mark">“</span>RAISED ON<br>CARE, PROVEN<br>THROUGH<br>SEASONS<span class="motto__mark" style="margin-top:6px">”</span></p>

  <div class="photo photo--back-house" role="img" aria-label="Photo of a blue two-storey house with white trim and front steps"></div>

  <div class="partners">
    <span class="partner"><i></i>NWTG</span>
    <span class="partner"><i></i>QCR</span>
    <span class="partner"><i></i>KOV</span>
    <span class="partner"><i></i>Owen Brisket</span>
  </div>

  <p class="offer offer__lead">We are in your area</p>
  <p class="offer offer__main">contact us today</p>
  <p class="offer offer__sub">for your Exclusive limited time offer</p>
  <p class="offer offer__note">*discounts apply exclusively to new agreements only</p>

  <div class="footer-band"></div>
  <p class="estimates">FREE ESTIMATES</p>
  <p class="phone"><svg width="30" height="30" viewBox="0 0 30 30" aria-hidden="true"><circle cx="15" cy="15" r="15" fill="#fff"/><path d="M10.5 7.5l3 3.5-1.8 2.2c1 2 2.6 3.6 4.6 4.6l2.2-1.8 3.5 3-1.8 2.8c-6.5-.5-11.8-5.8-12.3-12.3z" fill="var(--blue)"/></svg>403-555-0148</p>
  <p class="website">www.pellmontshingleworks.com</p>
</section>

</body>
</html>
```